Home Accessibility

Sturdy Hearth Builders (SHB) is a specialty construction company specializing in building custom homes and home modifications for individuals that are “Aging in Place” or with disabilities.
SHB is a full service construction company specializing in making independence accessible by helping people plan for now and the future. We provide a number of building services from custom designing a new home to modifying an existing home. SHB is a Licensed Lifelong Living Expert (LLLE). As a LLLE specialist, SHB is able to offer specialized strategies and techniques for designing and building aesthetically enriching living environments.
Marcus has been in the building industry for over 18 years; He has served on the board of the Dwelling Crafters Guild. He is Licensed Lifelong Living Expert (LLLE). Certified, also as Eco Framing for Trade Practitioners and a member of the Fair Trade Council (FTC)

I am looking for a promo piece where we install 2- 24" Vardel grab bars for $149.00
We can also do a free home evaluation which will show what or if any other modification or feature would be beneficial to them and the home.

Target Market(s)

Age 65+, disable, children of 65+

Industry/Entity Type

Construction

Requirements
Nice to have
• I would like to incorporate some or all of the bullet points from my mailer

```html
<!DOCTYPE html>
<html lang="en">
<head>
<meta charset="utf-8">
<title>Home Accessibility – Fall Prevention</title>
<link rel="stylesheet" href="https://fonts.googleapis.com/css2?family=Arimo:wght@400;700&family=Great+Vibes&display=swap">
<style>
  :root {
    --navy: #13253a;
    --navy-soft: #1d3a57;
    --lime: #aebb38;
    --olive: #8f9c3d;
    --petal-light: #bcc54c;
    --white: #ffffff;
    --ring-grey: #d9d9d9;
    --ink: #1b2230;
    --accent-text: #95a43c;
    --rule: #2c4260;
  }
  html, body {
    margin: 0;
    padding: 0;
    width: 1200px;
    height: 931px;
    overflow: hidden;
    background: var(--navy);
  }
  .poster {
    position: relative;
    width: 1200px;
    height: 931px;
    overflow: hidden;
    font-family: "Arimo", Arial, sans-serif;
  }
  .hero-photo {
    position: absolute;
    left: 0; top: 0;
    width: 1200px;
    height: 520px;
    background:
      radial-gradient(ellipse at 45% 30%, #b8a98a 0%, #8c7f60 30%, transparent 60%),
      radial-gradient(ellipse at 80% 35%, #a59674 0%, transparent 45%),
      linear-gradient(180deg, #3f3f2c 0%, #5a5639 50%, #4a4a33 100%);
  }
  .wave, .stat-badge {
    position: absolute;
    left: 0; top: 0;
  }
  .stat-text {
    position: absolute;
    left: 516px;
    top: 350px;
    width: 220px;
    text-align: center;
    color: var(--ink);
  }
  .stat-figure {
    display: block;
    font-size: 72px;
    line-height: 1;
    color: var(--lime);
  }
  .stat-label {
    display: block;
    font-size: 33px;
    line-height: 1.1;
    margin-top: 2px;
  }
  .stat-label-small {
    display: block;
    font-size: 23px;
    line-height: 1.3;
    margin-top: 2px;
  }
  .tips {
    position: absolute;
    left: 200px;
    top: 628px;
    width: 850px;
    text-align: center;
  }
  .tips-heading {
    margin: 0;
    font-family: "Great Vibes", cursive;
    font-weight: 400;
    font-size: 50px;
    line-height: 1.1;
    color: var(--white);
  }
  .tips-list {
    list-style: none;
    margin: 2px 0 0;
    padding: 0;
    font-size: 24px;
    font-weight: 700;
    line-height: 28px;
    color: var(--accent-text);
  }
  .offer {
    position: absolute;
    left: 150px;
    top: 800px;
    width: 900px;
    padding-top: 18px;
    border-top: 2px solid var(--rule);
    text-align: center;
    color: var(--white);
  }
  .offer-deal {
    margin: 0;
    font-size: 26px;
    font-weight: 700;
    line-height: 1.2;
  }
  .offer-price {
    color: var(--lime);
  }
  .offer-extra {
    margin: 8px 0 0;
    font-size: 19px;
    font-weight: 400;
    line-height: 1.3;
    color: var(--ring-grey);
  }
  .offer-cta {
    color: var(--lime);
    font-weight: 700;
  }
</style>
</head>
<body>
<main class="poster">
  <div class="hero-photo" role="img" aria-label="Close-up of an older person's hands resting on a walking cane"></div>

  <svg class="wave" width="1200" height="931" viewBox="0 0 1200 931" aria-hidden="true">
    <path d="M0,418 C150,408 300,478 600,478 C900,478 1050,413 1200,413 L1200,931 L0,931 Z" fill="var(--navy)"/>
    <path d="M0,404 C150,394 300,464 600,464 C900,464 1050,399 1200,399" fill="none" stroke="var(--lime)" stroke-width="26"/>
  </svg>

  <svg class="stat-badge" width="1200" height="931" viewBox="0 0 1200 931" aria-hidden="true">
    <circle cx="635" cy="300" r="68" fill="var(--navy)"/>
    <circle cx="507" cy="326" r="47" fill="var(--white)"/>
    <circle cx="779" cy="405" r="42" fill="var(--olive)"/>
    <circle cx="700" cy="553" r="58" fill="var(--navy-soft)"/>
    <circle cx="547" cy="542" r="45" fill="var(--petal-light)"/>
    <circle cx="479" cy="460" r="61" fill="var(--olive)"/>
    <circle cx="628" cy="432" r="118" fill="var(--white)"/>
    <circle cx="628" cy="432" r="108" fill="none" stroke="var(--ring-grey)" stroke-width="2"/>
    <circle cx="628" cy="432" r="110" fill="none" stroke="var(--lime)" stroke-width="14"
            stroke-dasharray="230 1000" transform="rotate(-90 628 432)"/>
    <circle cx="628" cy="432" r="103" fill="var(--white)"/>
  </svg>

  <div class="stat-text">
    <span class="stat-figure">33%</span>
    <span class="stat-label">of adults age</span>
    <span class="stat-label-small">65 and older falls.</span>
  </div>

  <section class="tips">
    <h1 class="tips-heading">Make homes safer by reducing tripping hazards</h1>
    <ul class="tips-list">
      <li>Install GRAB BARS</li>
      <li>Install RAILINGS</li>
      <li>improving the LIGHTING in homes.</li>
    </ul>
  </section>

  <section class="offer">
    <p class="offer-deal">Two 24" Vardel grab bars installed for <span class="offer-price">$149.00</span></p>
    <p class="offer-extra">Plus a FREE home evaluation. <span class="offer-cta">Call Sturdy Hearth Builders (SHB) today.</span></p>
  </section>
</main>
</body>
</html>
```